exclusive Speakeasy Bar Web design in New Jersey USA

We are opening a speakeasy in New Jersey USA soon. we are looking for a web designer to do our web site including the coding. we a looking for a 4 to 5 page web design. the site will be mostly static. home page, contact page, menu page and a link to a 3rd party site (most likely Qelmo) for reservations. we are looking for this designer to do our menu deign as well. we are looking for a quick turnaround 7-10 days. i am attaching some pictures for the designers to see the concept design and the actual current pictures with our logo as well. professionally taken pictures will be provided later on. our photographer will be taking the pictures in the next week.

Industry/Entity Type

Restaurant, Bar, Speakeasy

Coding

Coded - Design and coding required

Number of Pages Required

4 page

Requirements
Must have
• home page, contact page, menu page and a link to qelmo.com for reservations
Nice to have
• some videos

```html
<!DOCTYPE html>
<html lang="en">
<head>
<meta charset="utf-8">
<title>Nine Lantern – Menus</title>
<link rel="stylesheet" href="https://fonts.googleapis.com/css2?family=Lora:wght@400;500&family=Poppins:wght@300;400&display=swap">
<style>
  :root {
    --gold: #b8944f;
    --ink: #1b1b1b;
    --body: #3a3a3a;
    --cream: #fcf9f4;
    --cream-deep: #f9f4ec;
    --rule: #e3d3b6;
    --white: #ffffff;
    --night: #16161b;
  }
  * { box-sizing: border-box; margin: 0; padding: 0; }
  html, body { width: 821px; height: 1200px; overflow: hidden; }
  body { position: relative; background: var(--cream); font-family: "Poppins", sans-serif; color: var(--body); }
  .abs { position: absolute; }

  .hero { left: 0; top: 0; width: 821px; height: 308px;
    background: linear-gradient(180deg, #14141a 0%, #3b2a1d 35%, #5a3f27 60%, #2c2018 100%); }
  .header-rule { left: 0; width: 821px; height: 1px; background: var(--gold); }
  .nav a { position: absolute; top: 41px; font-size: 9.3px; color: var(--white); text-decoration: none; letter-spacing: .2px; }
  .nav a.active { color: var(--gold); }
  .brand { left: 381px; top: 8px; width: 58px; height: 76px; border: 1px solid var(--gold); background: var(--night);
    display: flex; align-items: center; justify-content: center; text-align: center;
    font-family: "Lora", serif; font-size: 10px; line-height: 1.25; color: var(--white); letter-spacing: .5px; }
  .social { top: 37px; width: 20px; height: 20px; border-radius: 50%; border: 1px solid var(--gold); }
  .social.filled { background: var(--gold); }

  .page-title { left: 337px; top: 166px; width: 149px; height: 36px; border: 1px solid var(--gold);
    font-family: "Lora", serif; font-size: 26px; font-weight: 500; color: var(--white);
    display: flex; align-items: center; justify-content: center; letter-spacing: .5px; }
  .corner { width: 7px; height: 7px; border: 1px solid var(--gold); }

  .feature-photo { left: 194px; top: 349px; width: 433px; height: 282px;
    background: radial-gradient(circle at 62% 45%, #a3582c 0%, #5a3420 18%, #1d1b1d 45%, #101418 100%); }

  .arrow { top: 480px; }

  .tab { top: 667px; height: 26px; border: 1px solid var(--gold); border-top-color: transparent;
    color: var(--gold); font-size: 8.5px; display: flex; align-items: center; justify-content: center; letter-spacing: .3px; }
  .tab::before { content: ""; position: absolute; top: -1px; left: 3px; right: 0; height: 1px; background: var(--gold); }

  .menu-section { left: 0; top: 739px; width: 821px; height: 435px; background: var(--cream-deep); }
  .section-title { left: 42px; top: 772px; font-family: "Lora", serif; font-size: 17.5px; color: var(--ink); }
  .section-rule { left: 41px; top: 803px; width: 739px; height: 1px; background: var(--rule); }

  .item { width: 300px; }
  .item.right { width: 352px; }
  .item-head { display: flex; justify-content: space-between; font-family: "Lora", serif; font-size: 12.4px; color: var(--ink); }
  .item-price { color: var(--gold); }
  .item-desc { margin-top: 9px; font-size: 8.8px; line-height: 14.5px; width: 215px; color: var(--body); }
  .item-rule { height: 1px; background: var(--rule); }

  .footer { left: 0; top: 1174px; width: 821px; height: 26px; background: var(--white);
    font-size: 8.8px; color: var(--ink); text-align: center; line-height: 24px; }
</style>
</head>
<body>
  <div class="abs hero" role="img" aria-label="Back bar shelves lined with liquor bottles in warm low light"></div>
  <div class="abs header-rule" style="top:21px"></div>
  <div class="abs header-rule" style="top:71px"></div>

  <nav class="nav">
    <a class="active" href="#" style="left:71px">HOME</a>
    <a href="#" style="left:165px">MENU</a>
    <a href="#" style="left:252px">CONTACT US</a>
  </nav>

  <div class="abs brand">NINE<br>LANTERN</div>

  <span class="abs social filled" style="left:709px" aria-label="Social link"></span>
  <span class="abs social" style="left:734px" aria-label="Social link"></span>
  <span class="abs social" style="left:759px" aria-label="Social link"></span>

  <span class="abs corner" style="left:330px;top:159px"></span>
  <h1 class="abs page-title">MENUS</h1>
  <span class="abs corner" style="left:487px;top:203px"></span>

  <div class="abs feature-photo" role="img" aria-label="Amber cocktail in a martini glass on a dark wooden bar"></div>

  <svg class="abs arrow" style="left:96px" width="44" height="28" viewBox="0 0 44 28" aria-label="Previous">
    <rect x="15" y="1" width="26" height="26" fill="none" stroke="#1b1b1b" stroke-width="1.2"/>
    <path d="M2 14H30M7 9L2 14L7 19" fill="none" stroke="#1b1b1b" stroke-width="1.2"/>
  </svg>
  <svg class="abs arrow" style="left:679px" width="44" height="28" viewBox="0 0 44 28" aria-label="Next">
    <rect x="1" y="1" width="26" height="26" fill="none" stroke="#b8944f" stroke-width="1.2"/>
    <path d="M13 14H42M37 9L42 14L37 19" fill="none" stroke="#b8944f" stroke-width="1.2"/>
  </svg>

  <span class="abs corner" style="left:246px;top:661px;width:6px;height:6px"></span>
  <a class="abs tab" style="left:251px;width:109px">COCKTAILS</a>
  <span class="abs corner" style="left:359px;top:692px;width:6px;height:6px"></span>
  <a class="abs tab" style="left:380px;width:91px">WINE&amp;BEER</a>
  <a class="abs tab" style="left:483px;width:92px">SPIRITS</a>

  <section class="abs menu-section"></section>
  <h2 class="abs section-title">Themed Cocktails</h2>
  <div class="abs section-rule"></div>

  <div class="abs item" style="left:42px;top:824px"><div class="item-head"><span>Regret Me Not</span><span class="item-price">$ 14</span></div><p class="item-desc">Lorem Ipsum is simply dummy text of the printing and typesetting industry.</p></div>
  <div class="abs item right" style="left:423px;top:824px;width:346px"><div class="item-head"><span>Regret Me Not</span><span class="item-price">$ 14</span></div><p class="item-desc">Lorem Ipsum is simply dummy text of the printing and typesetting industry.</p></div>
  <div class="abs item-rule" style="left:41px;top:900px;width:308px"></div>
  <div class="abs item-rule" style="left:421px;top:900px;width:359px"></div>

  <div class="abs item" style="left:42px;top:919px"><div class="item-head"><span>Regret Me Not</span><span class="item-price">$ 14</span></div><p class="item-desc">Lorem Ipsum is simply dummy text of the printing and typesetting industry.</p></div>
  <div class="abs item right" style="left:423px;top:919px;width:346px"><div class="item-head"><span>Regret Me Not</span><span class="item-price">$ 14</span></div><p class="item-desc">Lorem Ipsum is simply dummy text of the printing and typesetting industry.</p></div>
  <div class="abs item-rule" style="left:41px;top:1003px;width:308px"></div>
  <div class="abs item-rule" style="left:421px;top:1008px;width:359px"></div>

  <div class="abs item" style="left:42px;top:1029px"><div class="item-head"><span>Regret Me Not</span><span class="item-price">$ 14</span></div><p class="item-desc">Lorem Ipsum is simply dummy text of the printing and typesetting industry.</p></div>
  <div class="abs item right" style="left:423px;top:1029px;width:346px"><div class="item-head"><span>Regret Me Not</span><span class="item-price">$ 14</span></div><p class="item-desc">Lorem Ipsum is simply dummy text of the printing and typesetting industry.</p></div>
  <div class="abs item-rule" style="left:41px;top:1123px;width:308px"></div>
  <div class="abs item-rule" style="left:421px;top:1123px;width:359px"></div>

  <footer class="abs footer">© 2023&nbsp; NINE LANTERN. All Right Reserved.</footer>
</body>
</html>
```